New web design for a service provider in the medical field

We are looking for a new design for our website. We are a company that repairs and sells medical endoscopes. Our customers include doctors and hospitals. Our current website can be found at https://lumenfix.example/en/lumenfix-english.
We need a new web design (without programming) for the following 3 pages:
-Startpage https://lumenfix.example/en/lumenfix-english/
-Used endoscopes https://lumenfix.example/en/used-endoscopes/
-Purchase https://lumenfix.example/en/purchase/
The design should be modern and stylish.
The blue color of the logo should be reflected on the page, but not too intrusive.
I have uploaded the images from the header. If more images are needed, let me know and I will upload them.

Target Market(s)
Doctors and hospitals

```html
<!DOCTYPE html>
<html lang="en">
<head>
<meta charset="utf-8">
<title>LumenFix – Endoscope Repair</title>
<link href="https://fonts.googleapis.com/css2?family=Rubik:wght@400;500;600;700&family=Roboto:wght@400;500;700&display=swap" rel="stylesheet">
<style>
:root{
  --navy:#0e2a44;
  --navy-deep:#0b2238;
  --blue:#1ea6e0;
  --blue-dark:#146f9f;
  --heading:#17567e;
  --ink:#3a4a58;
  --muted:#6b7884;
  --pale:#eef6fa;
  --white:#ffffff;
}
*{margin:0;padding:0;box-sizing:border-box}
html,body{width:1200px;height:5025px;overflow:hidden}
body{font-family:'Roboto',sans-serif;color:var(--ink);background:var(--white);position:relative}
.section{position:absolute;left:0;width:1200px;overflow:hidden}
.abs{position:absolute}
.h-font{font-family:'Rubik',sans-serif}
.btn{position:absolute;display:flex;align-items:center;justify-content:center;font-family:'Rubik',sans-serif;font-weight:500;font-size:14px;letter-spacing:.5px;text-transform:uppercase;text-decoration:none}
.btn-solid{background:var(--blue);color:var(--white);border-radius:3px}
.btn-outline{border:1.5px solid var(--blue);color:var(--blue);border-radius:3px;background:transparent}
.btn-ghost{border:2px solid var(--white);color:var(--white);border-radius:3px}
.center{left:0;width:1200px;text-align:center}

/* top bar */
.topbar{top:0;height:32px;background:var(--navy-deep);color:var(--white);font-size:11px}
.topbar .item{position:absolute;top:9px;display:flex;align-items:center;gap:6px}
.topbar .link{position:absolute;top:10px;font-size:9.5px;font-weight:500;text-transform:uppercase}
.dot{width:12px;height:12px;border-radius:50%;border:1.5px solid var(--white);position:absolute;top:10px}

/* hero */
.hero{top:32px;height:641px}
.hero-photo{position:absolute;inset:0;background:linear-gradient(100deg,#0d2d4e 0%,#164b78 45%,#2d6d9c 70%,#1d4f7c 100%)}
.brand{position:absolute;display:flex;align-items:center;gap:8px;font-family:'Rubik',sans-serif;font-weight:600}
.brand .mark{width:10px;height:10px;border-radius:50%;background:var(--blue)}
.nav a{position:absolute;top:44px;color:var(--white);font-family:'Rubik',sans-serif;font-weight:500;font-size:10.5px;text-transform:uppercase;text-decoration:none}
.hero .welcome{left:88px;top:230px;color:var(--white);font-size:25px;font-weight:400}
.hero h1{left:88px;top:262px;color:var(--white);font-family:'Rubik',sans-serif;font-weight:600;font-size:60px;line-height:70px}

/* intro */
.intro{top:673px;height:371px}
.intro h2{top:70px;font-family:'Rubik',sans-serif;font-weight:700;font-size:50px;color:var(--heading)}
.intro p{top:166px;left:310px;width:580px;text-align:center;font-size:12.5px;line-height:21px;color:var(--muted)}

/* split */
.split{top:1044px;height:478px;background:var(--pale)}
.split-photo{position:absolute;left:0;top:0;width:527px;height:478px;background:linear-gradient(135deg,#dde6ee,#9fb4c6 50%,#cbd6df)}
.split h3{left:599px;top:56px;width:520px;font-family:'Rubik',sans-serif;font-weight:600;font-size:24px;line-height:31px;color:var(--heading)}
.split p{left:599px;width:510px;font-size:11.5px;line-height:20px;color:var(--ink)}

/* makers */
.makers{top:1522px;height:148px}
.maker{position:absolute;top:50px;font-family:'Rubik',sans-serif;font-weight:700;font-size:32px;color:var(--navy)}

/* offer */
.offer{top:1670px;height:593px;background:var(--pale)}
.offer h2{top:58px;font-family:'Rubik',sans-serif;font-weight:600;font-size:29px;color:var(--heading)}
.card{position:absolute;top:139px;width:326px;height:357px;background:var(--white);box-shadow:0 4px 20px rgba(20,80,120,.08)}
.card .tag{position:absolute;left:25px;top:31px;font-family:'Rubik',sans-serif;font-weight:600;font-size:12px;color:var(--blue);letter-spacing:.5px}
.card h4{position:absolute;left:25px;top:56px;font-family:'Rubik',sans-serif;font-weight:600;font-size:25px;line-height:26px;color:var(--heading)}
.card p{position:absolute;left:25px;top:130px;width:280px;font-size:11.5px;line-height:20.5px;color:var(--muted)}
.card .btn{left:25px;top:264px;width:183px;height:54px}

/* faulty */
.faulty{top:2263px;height:470px}
.dark-photo{position:absolute;inset:0;background:linear-gradient(120deg,#1d3a55,#2b4f6d 50%,#1a3550)}
.faulty h2{top:110px;color:var(--white);font-family:'Rubik',sans-serif;font-weight:600;font-size:50px}
.faulty .sub{top:186px;color:var(--white);font-family:'Rubik',sans-serif;font-size:25px}
.faulty .note{top:234px;color:var(--blue);font-family:'Rubik',sans-serif;font-weight:500;font-size:19px}

/* outcome */
.outcome{top:2733px;height:705px}
.outcome h2{top:64px;font-family:'Rubik',sans-serif;font-weight:600;font-size:29px;color:var(--heading)}
.hub{position:absolute;left:420px;top:209px;width:370px;height:370px;border-radius:50%;background:var(--white);box-shadow:0 0 40px rgba(30,120,170,.08)}
.bubble{position:absolute;width:124px;height:124px;border-radius:50%;display:flex;align-items:center;justify-content:center;text-align:center;color:var(--white);font-family:'Rubik',sans-serif;font-weight:600;font-size:12.5px;line-height:18px;padding:14px}
.b1{background:#1d9bd6}.b2{background:#2aa7dc}.b3{background:#1786c2}.b4{background:#5bbbe4}.b5{background:#1a6f9e}.b6{background:#1679b0}

/* benefits */
.benefits{top:3438px;height:799px}
.benefits h2{top:78px;font-family:'Rubik',sans-serif;font-weight:600;font-size:28px;line-height:33px;color:var(--heading)}
.feat{position:absolute;width:270px;text-align:center}
.feat svg{display:block;margin:0 auto}
.feat h5{font-family:'Rubik',sans-serif;font-weight:600;font-size:14px;color:var(--blue-dark);margin:10px 0 6px}
.feat p{font-size:11.5px;line-height:21px;color:var(--muted)}

/* help */
.help{top:4237px;height:344px}
.help h2{top:94px;color:var(--white);font-family:'Rubik',sans-serif;font-weight:600;font-size:50px}

/* footer */
.footer{top:4581px;height:444px;background:var(--navy-deep);color:#c7d3de}
.footer .call{left:84px;top:42px;font-family:'Rubik',sans-serif;font-weight:600;font-size:17px;color:var(--white)}
.footer .phone{left:775px;top:30px;font-family:'Rubik',sans-serif;font-weight:500;font-size:31px;color:var(--blue)}
.footer .rule{left:84px;top:100px;width:1032px;height:1px;background:rgba(255,255,255,.12)}
.fcol{position:absolute;top:164px}
.fcol h6{font-family:'Rubik',sans-serif;font-weight:600;font-size:13.5px;color:var(--white);margin-bottom:26px}
.fcol li{list-style:none;font-size:11.5px;line-height:27px}
.footer .copy{top:411px;font-size:10.5px}
.fsoc{position:absolute;top:305px;width:14px;height:14px;border-radius:50%;border:1.5px solid #c7d3de}
</style>
</head>
<body>

<header class="section topbar">
  <div class="item" style="left:84px"><svg width="13" height="10" viewBox="0 0 13 10"><rect x=".7" y=".7" width="11.6" height="8.6" fill="none" stroke="#fff" stroke-width="1.2"/><path d="M1 1l5.5 4.5L12 1" fill="none" stroke="#fff" stroke-width="1.2"/></svg>info@lumenfix.example</div>
  <div class="item" style="left:273px"><svg width="9" height="13" viewBox="0 0 9 13"><rect x=".7" y=".7" width="7.6" height="11.6" rx="1.5" fill="none" stroke="#fff" stroke-width="1.2"/><circle cx="4.5" cy="10" r=".8" fill="#fff"/></svg>+49 4100 555 210-0</div>
  <span class="link" style="left:692px">Pick-up order</span>
  <span class="link" style="left:816px">About us</span>
  <span class="link" style="left:908px">Contact us</span>
  <span class="dot" style="left:1004px"></span>
  <span class="dot" style="left:1034px"></span>
  <span class="dot" style="left:1066px"></span>
  <span class="dot" style="left:1098px"></span>
</header>

<section class="section hero">
  <div class="hero-photo" role="img" aria-label="Endoscope equipment in a clinical room, blue tinted"></div>
  <div class="brand" style="left:95px;top:40px;color:#fff;font-size:15px"><span class="mark"></span>LumenFix</div>
  <nav class="nav">
    <a style="left:313px">Endoscope repair</a>
    <a style="left:457px">Used endoscopes</a>
    <a style="left:594px">Endoscopy systems</a>
    <a style="left:733px">Endoscopy accessories</a>
    <a style="left:909px">Accessories catalog</a>
    <a style="left:1054px">Purchase</a>
  </nav>
  <p class="abs welcome">Welcome to LumenFix</p>
  <h1 class="abs">Put Your Endoscope<br>in Relaible Hands !</h1>
  <a class="btn btn-ghost" style="left:88px;top:440px;width:191px;height:61px">Contact now</a>
</section>

<section class="section intro">
  <h2 class="abs center">Your Future - Our Service</h2>
  <p class="abs">LumenFix GmbH is specialised in the repair and sale of Aurelis, Kestrel and Novaris flexible medical endoscopes. As a service-oriented company, we are at your side with our knowledge and skills!</p>
  <a class="btn btn-outline" style="left:490px;top:264px;width:193px;height:62px">More details</a>
</section>

<section class="section split">
  <div class="split-photo" role="img" aria-label="Endoscope testing workstation with instruments and gauges"></div>
  <h3 class="abs">Endoscope repairs and second hand en-doscopes from LumenFix – cause the outcome matters!</h3>
  <p class="abs" style="top:170px">LumenFix is a privileged partner for the start-up facility or optimisation of existing healthcare facilities, doctor's offices and hospitals. The quality and reliability of our products and our offered service are our best advertisement!</p>
  <p class="abs" style="top:250px">As a result of optimised processes and highly qualified specialists in our company, we can work very quickly and with high quality for your benefit of least possible restrictions in your doctor's office or in your hospital.</p>
  <a class="btn btn-solid" style="left:599px;top:359px;width:191px;height:62px">More details</a>
</section>

<section class="section makers">
  <span class="maker" style="left:244px">AURELIS</span>
  <span class="maker" style="left:513px">KESTREL</span>
  <span class="maker" style="left:751px">NOVARIS</span>
</section>

<section class="section offer">
  <h2 class="abs center">What We Offer</h2>
  <article class="card" style="left:88px">
    <span class="tag">REPAIR</span>
    <h4>Endoscope<br>Repair Service</h4>
    <p>Manufacturer-independent we repair and maintain endoscopes, individual components (e.g. processors or light sources), accessories and peripherals of the manufacturers Aurelis, Kestrel and Novaris.</p>
    <a class="btn btn-solid">Repair request</a>
  </article>
  <article class="card" style="left:439px">
    <span class="tag">SALE</span>
    <h4>Sale Used<br>Endoscopes</h4>
    <p>Our regular stock includes refurbished gastroscopes, coloscopes, bronchoscopes, cystoscopes and duodenoscopes from the well-known manufacturers Aurelis, Kestrel and Novaris.</p>
    <a class="btn btn-solid">Purchase request</a>
  </article>
  <article class="card" style="left:790px">
    <span class="tag">PURCHASE</span>
    <h4>Purchase Used<br>Endoscopes</h4>
    <p>We are very interested in buying your old endoscopes – even defective and dismantled! We offer fair conditions! Please contact us for a purchase offer!</p>
    <a class="btn btn-solid">Sell request</a>
  </article>
</section>

<section class="section faulty">
  <div class="dark-photo" role="img" aria-label="Technician holding an endoscope, dark blue overlay"></div>
  <h2 class="abs center">Faulty Endoscope ?</h2>
  <p class="abs center sub">We ensure quick and smooth repairs!</p>
  <p class="abs center note">Simple place a pick-up order</p>
  <a class="btn btn-solid" style="left:509px;top:289px;width:182px;height:51px">Pickup order</a>
</section>

<section class="section outcome">
  <h2 class="abs center">Cause The Outcome Matters</h2>
  <div class="hub"></div>
  <div class="brand" style="left:527px;top:382px;color:var(--navy);font-size:22px"><span class="mark"></span>LumenFix</div>
  <div class="bubble b1" style="left:547px;top:151px">Experience Characterises Us</div>
  <div class="bubble b2" style="left:369px;top:215px">One company for everyone</div>
  <div class="bubble b3" style="left:718px;top:235px">The Product is Close to Our Hearts</div>
  <div class="bubble b4" style="left:359px;top:432px">Guaranteed Service</div>
  <div class="bubble b5" style="left:703px;top:428px">Services For Everyone</div>
  <div class="bubble b6" style="left:541px;top:535px">Quality Not Quantity</div>
</section>

<section class="section benefits">
  <h2 class="abs center">LumenFix GmbH,<br>your decision for your future</h2>
  <div class="feat" style="left:119px;top:210px">
    <svg width="46" height="46" viewBox="0 0 46 46" fill="none" stroke="#1ea6e0" stroke-width="2.5"><circle cx="23" cy="23" r="20"/><path d="M23 11v12l8 6"/></svg>
    <h5>Fast repairs</h5>
    <p>Keep potential disruptions in your doctor's office or in your hospital at minimum as a result of optimized processes and highly qualified specialists in our company</p>
  </div>
  <div class="feat" style="left:466px;top:210px">
    <svg width="46" height="46" viewBox="0 0 46 46" fill="none" stroke="#1ea6e0" stroke-width="2.5"><path d="M5 22L23 6l18 16M10 18v22h26V18"/><path d="M19 40V28h8v12"/></svg>
    <h5>On-site service</h5>
    <p>We will gladly pay you a visit to to carry out analysis and repairs on site. Due to our many years of experience – it doesn't get any faster (whigleithin a 250 km range)</p>
  </div>
  <div class="feat" style="left:829px;top:210px">
    <svg width="46" height="46" viewBox="0 0 46 46" fill="none" stroke="#1ea6e0" stroke-width="2.5"><circle cx="23" cy="23" r="20"/><path d="M14 23l7 7 13-14"/></svg>
    <h5>Without a maintenance<br>contract</h5>
    <p>No subscription or other maintenance contract, but one-time and sustainable repair work</p>
  </div>
  <div class="feat" style="left:119px;top:452px">
    <svg width="46" height="46" viewBox="0 0 46 46" fill="none" stroke="#1ea6e0" stroke-width="2.5"><path d="M10 4h18l8 8v30H10z"/><path d="M27 19h-6a3 3 0 000 6h4a3 3 0 010 6h-7M23 16v18"/></svg>
    <h5>Highly cost efficient</h5>
    <p>Benefit from our first class recommendations and implementation by our experienced staff. Our goals is to find the best solutions together with you at the best lowest price point.</p>
  </div>
  <div class="feat" style="left:466px;top:452px">
    <svg width="46" height="46" viewBox="0 0 46 46" fill="none" stroke="#1ea6e0" stroke-width="2.5"><rect x="4" y="9" width="38" height="26" rx="2"/><path d="M4 17h38"/><path d="M24 31l5 5 10-10"/></svg>
    <h5>Loan equipment service</h5>
    <p>Use our service of high-quality loan devices during the downtime of your defective endoscope (limited to stock)</p>
  </div>
  <div class="feat" style="left:829px;top:452px">
    <svg width="46" height="46" viewBox="0 0 46 46" fill="none" stroke="#1ea6e0" stroke-width="2.5"><rect x="4" y="20" width="8" height="20"/><path d="M12 22l8-16c4 0 5 3 4 7l-2 6h14c3 0 4 3 3 5l-4 14c-1 2-2 3-4 3H12"/></svg>
    <h5>First class service</h5>
    <p>Our clients always come first!</p>
  </div>
  <a class="btn btn-solid" style="left:509px;top:679px;width:182px;height:54px">More about us</a>
</section>

<section class="section help">
  <div class="dark-photo" role="img" aria-label="Handshake in a business setting, dark blue overlay"></div>
  <h2 class="abs center">How Can We Help You ?</h2>
  <a class="btn btn-solid" style="left:509px;top:192px;width:182px;height:54px">Send message</a>
</section>

<footer class="section footer">
  <p class="abs call">FIND AN ENDOSPIC. CALL US ANYTIME!</p>
  <p class="abs phone">+49 4100 555 210-0</p>
  <div class="abs rule"></div>
  <div class="fcol" style="left:84px"><h6>COMPANY</h6><ul><li>About Us</li><li>Company</li><li>Press &amp; Blog</li><li>Privacy Policy</li><li>Faq</li></ul></div>
  <div class="fcol" style="left:341px"><h6>OPEN HOUR</h6><ul><li>Monday 11am–7pm</li><li>Tuesday-Friday 11am–8pm</li><li>Saturday 10am–6pm</li><li>Sunday 11am–6pm</li></ul></div>
  <div class="fcol" style="left:599px"><h6>RESOURCES</h6><ul><li>Home Insurance</li><li>Travel Insurance</li><li>Car Insurance</li><li>Business Insurance</li><li>Heal Insurance</li></ul></div>
  <div class="brand" style="left:862px;top:172px;color:#fff;font-size:15px"><span class="mark"></span>LumenFix</div>
  <p class="abs" style="left:855px;top:230px;width:250px;font-size:11.5px;line-height:21px">We have been providing quality to our customers</p>
  <span class="fsoc" style="left:852px"></span>
  <span class="fsoc" style="left:896px"></span>
  <span class="fsoc" style="left:941px"></span>
  <span class="fsoc" style="left:985px"></span>
  <p class="abs center copy">© 2022, lumenfix. All rights reserved.</p>
</footer>

</body>
</html>
```